Patternmaking service (fashion) card design

I need cards for my patternmaking service. I service both large and small fashion labels including ladies,mens and childrenswear. I would like cards that have a sort of vintage feel, especially 50's and 60's style. Pink is my signature colour. Its important to have a fashion reference of some kind.

Industry/Entity Type

Fashion

Contact Information for Business Card

Marigold Lantern, Patternmaking Service, Pennae Falcastro,
27 Wexbury Lane. Ashbrook Vale. NSW. 2741. 0415836204, email:spoolinda4@quillmail.example. "By appointment only"

```html
<!DOCTYPE html>
<html lang="en">
<head>
<meta charset="utf-8">
<title>Marigold Lantern – Business Card</title>
<link rel="stylesheet" href="https://fonts.googleapis.com/css2?family=Pacifico&family=Jost:wght@400;500&display=swap">
<style>
  :root {
    --page: #ffffff;
    --blush: #f7c9dd;
    --rose: #f5a7b1;
    --berry: #c96a77;
    --white: #ffffff;
  }
  html, body {
    margin: 0;
    padding: 0;
    width: 1200px;
    height: 1000px;
    overflow: hidden;
    background: var(--page);
  }
  .canvas {
    position: relative;
    width: 1200px;
    height: 1000px;
  }
  .card {
    position: absolute;
    left: 252px;
    top: 312px;
    width: 703px;
    height: 378px;
    background: var(--rose);
    overflow: hidden;
  }
  .card__top {
    position: absolute;
    left: 0; top: 0;
    width: 100%;
    height: 113px;
    background: var(--blush);
  }
  .card__cutline {
    position: absolute;
    left: 0;
    top: 110px;
    width: 703px;
    height: 6px;
  }
  .card__scissors {
    position: absolute;
    left: 0;
    top: 60px;
    width: 100px;
    height: 110px;
  }
  .brand {
    position: absolute;
    left: 0; right: 0;
    top: 8px;
    margin: 0;
    text-align: center;
    font-family: "Pacifico", cursive;
    font-weight: 400;
    font-size: 70px;
    line-height: 1.3;
    color: var(--berry);
  }
  .service {
    position: absolute;
    left: 0; right: 0;
    top: 130px;
    margin: 0;
    text-align: center;
    font-family: "Jost", sans-serif;
    font-weight: 400;
    font-size: 29px;
    letter-spacing: 0.27em;
    padding-left: 0.27em;
    color: var(--white);
  }
  .appointment__text {
    position: absolute;
    left: 0; right: 0;
    top: 208px;
    margin: 0;
    text-align: center;
    font-family: "Pacifico", cursive;
    font-size: 28px;
    line-height: 50px;
    color: var(--berry);
  }
  .appointment__ornament {
    position: absolute;
    top: 180px;
    width: 76px;
    height: 102px;
    border-radius: 50%;
    background: radial-gradient(circle, rgba(201,106,119,0.45) 0%, rgba(201,106,119,0.12) 70%, rgba(201,106,119,0) 100%);
  }
  .appointment__ornament--left { left: 118px; }
  .appointment__ornament--right { left: 498px; }
  .contact {
    position: absolute;
    left: 0; right: 0;
    top: 284px;
    margin: 0;
    text-align: center;
    font-family: "Jost", sans-serif;
    font-style: normal;
    font-size: 26px;
    line-height: 30px;
    color: var(--white);
  }
  .contact__gap { display: inline-block; width: 24px; }
</style>
</head>
<body>
<div class="canvas">
  <section class="card">
    <div class="card__top"></div>

    <svg class="card__cutline" viewBox="0 0 703 6" aria-hidden="true">
      <line x1="4" y1="3" x2="703" y2="3" stroke="var(--white)" stroke-width="2.5" stroke-dasharray="10 5"/>
    </svg>

    <svg class="card__scissors" viewBox="0 0 100 110" aria-hidden="true">
      <g fill="none" stroke="var(--white)" stroke-width="5">
        <ellipse cx="26" cy="28" rx="16" ry="9" transform="rotate(22 26 28)"/>
        <ellipse cx="30" cy="84" rx="17" ry="10" transform="rotate(-42 30 84)"/>
      </g>
      <g fill="var(--white)">
        <path d="M38 34 Q56 44 90 66 Q62 60 40 42 Z"/>
        <path d="M42 74 Q60 52 92 38 Q70 56 46 80 Z"/>
        <circle cx="57" cy="53" r="3.5"/>
      </g>
    </svg>

    <h1 class="brand">Marigold Lantern</h1>
    <p class="service">PATTERNMAKING SERVICE</p>

    <div class="appointment__ornament appointment__ornament--left" role="img" aria-label="Retro atomic starburst ornament"></div>
    <p class="appointment__text">By Appointment Only</p>
    <div class="appointment__ornament appointment__ornament--right" role="img" aria-label="Retro atomic starburst ornament"></div>

    <address class="contact">
      Pennae Falcastro<br>
      27 Wexbury Lane, Ashbrook Vale, NSW, 2741<br>
      M: 0415836204<span class="contact__gap"></span>E: spoolinda4@quillmail.example
    </address>
  </section>
</div>
</body>
</html>
```